Business Card Design Project - bel soravin group

dear Sirs

we need business card design for our group ( BEL Soravin Group ) , i have got the Logo design of our group from pixel harbor in previous , so all need details relating to our group i think available with you, as well as the the chosen logo design

we hope to provide us with business card logo that to be appropaite and satisfactory to us .

thanks

note : logo design of our group is attached .
Updates

Reason: please extend the deadline of my project for additional 15 days because i didn't received appropriate design for our gruop yet . kindly beaware that i have received 77 design till now , supossed to send me 200-250 design at least . thanks

Target Market(s)

contents
-

name : Korvan EL Mistrani

position : Operation Manager

Industry/Entity Type

Business

Requirements
Must have

• person name

group logo
Nice to have
• logo color matching with back background

```html
<!DOCTYPE html>
<html lang="en">
<head>
<meta charset="utf-8">
<title>BEL Soravin Group — Business Card</title>
<link rel="stylesheet" href="https://fonts.googleapis.com/css2?family=Jost:wght@400;500;600&family=Crimson+Text:wght@400;700&display=swap">
<style>
  :root {
    --bg: #e9e6e1;
    --navy: #0f4a8a;
    --navy-deep: #0a3466;
    --navy-light: #1c5fa6;
    --gold: #c9922f;
    --gold-soft: #e2c688;
    --cream: #f4e6c4;
    --ink: #555555;
    --paper: #ffffff;
  }
  * { margin: 0; padding: 0; box-sizing: border-box; }
  html, body { width: 1200px; height: 1137px; overflow: hidden; }
  body {
    background: var(--bg);
    font-family: "Jost", sans-serif;
    position: relative;
  }
  .card {
    position: absolute;
    left: 220px;
    width: 760px;
    height: 434px;
    overflow: hidden;
    box-shadow: 0 12px 30px rgba(0,0,0,0.18);
  }
  .card--front { top: 60px; background: var(--paper); }
  .card--back {
    top: 580px;
    background: radial-gradient(ellipse at 50% 35%, var(--navy-light) 0%, var(--navy) 45%, var(--navy-deep) 100%);
  }
  .gold-band {
    position: absolute;
    left: 0; right: 0; bottom: 0;
    height: 22px;
    background: linear-gradient(90deg, var(--gold-soft), var(--gold));
  }
  .brand {
    font-family: "Jost", sans-serif;
    font-weight: 600;
    text-transform: uppercase;
    letter-spacing: 0.02em;
    display: flex;
    align-items: center;
    gap: 10px;
    line-height: 1;
    white-space: nowrap;
  }
  .brand__mark { width: 14px; height: 14px; flex: none; }
  .card--front .brand {
    position: absolute;
    left: 36px; top: 164px;
    width: 350px;
    font-size: 26px;
    color: var(--navy);
  }
  .card--front .brand__mark { background: var(--gold); }
  .name-plate {
    position: absolute;
    left: 418px; top: 136px;
    width: 342px; height: 84px;
    background: var(--cream);
    padding: 12px 0 0 18px;
  }
  .name-plate__name {
    font-family: "Crimson Text", serif;
    font-weight: 700;
    font-size: 27px;
    color: var(--gold);
    line-height: 1.1;
    white-space: nowrap;
  }
  .name-plate__role {
    font-family: "Crimson Text", serif;
    font-size: 19px;
    color: var(--ink);
    margin-top: 2px;
  }
  .contact {
    position: absolute;
    left: 36px; top: 320px;
    font-size: 13.5px;
    color: var(--ink);
    list-style: none;
  }
  .contact__row { display: flex; align-items: center; margin-bottom: 8px; }
  .contact__item { display: flex; align-items: center; gap: 8px; white-space: nowrap; }
  .contact__item + .contact__item {
    margin-left: 12px; padding-left: 12px;
    border-left: 1px solid #cfcfcf;
  }
  .icon { width: 12px; height: 12px; fill: var(--navy); flex: none; }
  .card--back .brand {
    position: absolute;
    left: 0; right: 0; top: 180px;
    justify-content: center;
    font-size: 30px;
    color: var(--paper);
  }
  .card--back .brand__mark { background: var(--paper); }
  .website {
    position: absolute;
    left: 0; right: 0; top: 292px;
    text-align: center;
    font-size: 28px;
    letter-spacing: 0.04em;
    color: var(--gold);
  }
</style>
</head>
<body>

<section class="card card--front" aria-label="Business card front">
  <div class="brand"><span class="brand__mark"></span>BEL Soravin Group</div>

  <div class="name-plate">
    <p class="name-plate__name">Korvan EL Mistrani</p>
    <p class="name-plate__role">Operation Manager</p>
  </div>

  <ul class="contact">
    <li class="contact__row">
      <span class="contact__item">
        <svg class="icon" viewBox="0 0 12 12"><path d="M6 1 0.5 6H2v5h3V8h2v3h3V6h1.5z"/></svg>
        Lorem Ipsum is simply dummy text of the printing
      </span>
    </li>
    <li class="contact__row">
      <span class="contact__item">
        <svg class="icon" viewBox="0 0 12 12"><path d="M3.5 0h5a1 1 0 0 1 1 1v10a1 1 0 0 1-1 1h-5a1 1 0 0 1-1-1V1a1 1 0 0 1 1-1zm0 1.5v7.5h5V1.5z"/></svg>
        (000) 00 000 00 00
      </span>
      <span class="contact__item">
        <svg class="icon" viewBox="0 0 12 12"><path d="M3 1h5v3H3zM1 5h10v5H9V8H3v2H1zM3 9h6v3H3z"/></svg>
        (000) 00 000 00 00
      </span>
      <span class="contact__item">
        <svg class="icon" viewBox="0 0 12 12"><path d="M2.5 0.5 4.5 3 3.5 4.5c.8 1.7 2.2 3.1 4 4L9 7.5l2.5 2-1 2C5 11.5.5 7 .5 1.5z"/></svg>
        (000) 00 000 00 00
      </span>
    </li>
    <li class="contact__row">
      <span class="contact__item">
        <svg class="icon" viewBox="0 0 12 12"><path d="M0 2h12v8H0zm1 1 5 3.5L11 3z" fill-rule="evenodd"/></svg>
        korvan@bel-soravin.com
      </span>
    </li>
  </ul>

  <div class="gold-band"></div>
</section>

<section class="card card--back" aria-label="Business card back">
  <div class="brand"><span class="brand__mark"></span>BEL Soravin Group</div>
  <p class="website">www.bel-soravin.com</p>
  <div class="gold-band"></div>
</section>

</body>
</html>
```